RR Promotions a premium promotional agency needs design of business cards

I'm looking for a premium classy business card - possibly the Logo (the two backward R's) to be raised. Black and white for colour scheme would be preferable. I have attached my initial idea but open to your suggestions. We are a promotional agency who promote high profile brands. Thank you.

Contact Information for Business Card

TALIA BREWSTER
+64 21 507 9362
Talia@RRpromotions-example.net
www.RRpromotions-example.net

Colors
000000
ffffff

```html
<!DOCTYPE html>
<html lang="en">
<head>
<meta charset="utf-8">
<title>RR Promotions — Business Card</title>
<link rel="stylesheet" href="https://fonts.googleapis.com/css2?family=Roboto:wght@300;400;700&display=swap">
<style>
  :root {
    --backdrop: #d9d9db;
    --card-light: #2b2b2b;
    --card-dark: #0a0a0a;
    --ink-white: #ffffff;
    --ink-name: #b9b9bb;
    --ink-detail: #a9a9ab;
    --divider: rgba(255, 255, 255, 0.28);
  }
  * { box-sizing: border-box; margin: 0; padding: 0; }
  html, body {
    width: 1200px;
    height: 1200px;
    overflow: hidden;
    background: var(--backdrop);
    font-family: "Roboto", Arial, sans-serif;
  }
  .canvas {
    position: relative;
    width: 1200px;
    height: 1200px;
  }
  .card {
    position: absolute;
    left: 167px;
    width: 838px;
    height: 474px;
    background:
      radial-gradient(ellipse at 50% 0%, var(--card-light) 0%, var(--card-dark) 75%);
    overflow: hidden;
  }
  .card--front { top: 96px; }
  .card--back  { top: 602px; }

  /* Front */
  .front-brand {
    position: absolute;
    left: 0;
    top: 0;
    width: 324px;
    height: 474px;
    display: flex;
    align-items: center;
    justify-content: center;
    gap: 12px;
  }
  .front-brand__name {
    color: var(--ink-white);
    font-size: 30px;
    font-weight: 400;
    letter-spacing: 0.5px;
  }
  .front-divider {
    position: absolute;
    left: 324px;
    top: 36px;
    width: 2px;
    height: 352px;
    background: linear-gradient(to bottom, transparent, var(--divider) 35%, var(--divider) 65%, transparent);
  }
  .contact {
    position: absolute;
    left: 395px;
    top: 148px;
  }
  .contact__name {
    color: var(--ink-name);
    font-size: 32px;
    font-weight: 700;
    line-height: 1;
    margin-bottom: 16px;
  }
  .contact__line {
    color: var(--ink-detail);
    font-size: 26px;
    font-weight: 300;
    line-height: 1;
    margin-bottom: 22px;
    letter-spacing: 0.3px;
  }

  /* Back */
  .back-mark {
    position: absolute;
    left: 50%;
    top: 140px;
    width: 36px;
    height: 36px;
    margin-left: -18px;
    background: var(--ink-white);
  }
  .back-brand {
    position: absolute;
    left: 0;
    right: 0;
    top: 196px;
    text-align: center;
    color: var(--ink-white);
    font-size: 84px;
    font-weight: 400;
    line-height: 1;
  }
  .back-web {
    position: absolute;
    left: 0;
    right: 0;
    top: 372px;
    text-align: center;
    color: var(--ink-detail);
    font-size: 24px;
    font-weight: 400;
    letter-spacing: 0.5px;
  }
</style>
</head>
<body>
  <main class="canvas">
    <section class="card card--front">
      <div class="front-brand">
        <span class="front-brand__name">RR Promotions</span>
      </div>
      <div class="front-divider"></div>
      <div class="contact">
        <p class="contact__name">TALIA BREWSTER</p>
        <p class="contact__line">+64 21 507 9362</p>
        <p class="contact__line">Talia@RRpromotions-example.net</p>
        <p class="contact__line">www.RRpromotions-example.net</p>
      </div>
    </section>

    <section class="card card--back">
      <div class="back-mark"></div>
      <h1 class="back-brand">RR Promotions</h1>
      <p class="back-web">WWW.RRPROMOTIONS-EXAMPLE.NET</p>
    </section>
  </main>
</body>
</html>
```